New lease of life for a tired Country Pub menu, QLD

I need to refresh my menus with updated prices. The menus need to be A4 (the menus are laminated and handed out over the bar. I'd like to include our logo. I will upload our existing menus as well as the new prices. The design should be humble yet stylish if that's ok, please

Target Market(s)

Locals, travellers and workers

Industry/Entity Type

Hospitality, Quintessential Country pub

Font styles to use
Sans Serif

Colors

Designer to choose colors to be used in the design.

Requirements
Must have
• as we run different menus on different nights
Nice to have
• our logo

```html
<!DOCTYPE html>
<html lang="en">
<head>
<meta charset="utf-8">
<title>Saltbush Tavern – Lunch Menu</title>
<link rel="stylesheet" href="https://fonts.googleapis.com/css2?family=Poppins:wght@600;700;800&family=Fira+Sans+Condensed:wght@700&family=Jost:wght@400;500&display=swap">
<style>
  :root {
    --backdrop: #5a5a5a;
    --paper: #ffffff;
    --gold: #8a6a2c;
    --forest: #0d1a10;
    --ink: #111111;
    --bun: #d98a3a;
    --bun-dark: #a85a1e;
    --leaf: #5a9a36;
    --sauce: #c2281c;
  }
  * { box-sizing: border-box; margin: 0; padding: 0; }
  html, body { width: 965px; height: 1200px; overflow: hidden; background: var(--backdrop); }
  .canvas { position: relative; width: 965px; height: 1200px; }
  .menu-sheet { position: absolute; left: 112px; top: 89px; width: 741px; height: 1023px; background: var(--paper); overflow: hidden; }
  .menu-sheet > * { position: absolute; }

  .title { font-family: "Poppins", sans-serif; font-weight: 800; font-size: 90px; line-height: 1; letter-spacing: -1px; left: 40px; }
  .title--lunch { top: 28px; color: var(--gold); }
  .title--menu { top: 102px; color: var(--forest); }
  .service-note { left: 41px; top: 203px; font-family: "Poppins", sans-serif; font-weight: 700; font-size: 19.5px; line-height: 23.5px; color: var(--ink); letter-spacing: -0.2px; }

  .brand-band { left: 396px; top: 0; width: 286px; height: 128px; background: var(--forest); }
  .brand-name { left: 396px; top: 168px; width: 286px; text-align: center; font-family: "Poppins", sans-serif; font-weight: 700; font-size: 27px; line-height: 1.2; color: var(--forest); white-space: nowrap; }

  .photo { background: radial-gradient(ellipse at 50% 40%, #e7a04c 0%, var(--bun) 30%, var(--sauce) 52%, #5b3320 70%, var(--bun-dark) 85%, rgba(255,255,255,0) 100%); }
  .photo--right { left: 450px; top: 276px; width: 291px; height: 379px; border-radius: 46% 0 0 40%; }
  .photo--left { left: 0; top: 653px; width: 262px; height: 322px; border-radius: 0 48% 40% 0; background: radial-gradient(ellipse at 40% 50%, #f0b73a 0%, var(--sauce) 25%, var(--leaf) 45%, var(--bun) 65%, var(--bun-dark) 85%, rgba(255,255,255,0) 100%); }

  .section-label { font-family: "Fira Sans Condensed", sans-serif; font-weight: 700; font-size: 17px; color: var(--gold); line-height: 1; }
  .col-head { font-family: "Poppins", sans-serif; font-weight: 700; font-size: 9px; color: var(--gold); line-height: 1; text-align: center; width: 80px; }
  .rule { width: 1.5px; background: var(--gold); }

  .dish-name { font-family: "Fira Sans Condensed", sans-serif; font-weight: 700; font-size: 18.5px; line-height: 17px; color: var(--gold); letter-spacing: 0.5px; }
  .dish-desc { font-family: "Jost", sans-serif; font-weight: 400; font-size: 11.9px; line-height: 14px; color: var(--ink); }
  .addon { font-family: "Jost", sans-serif; font-weight: 500; font-size: 15px; line-height: 1; color: var(--ink); letter-spacing: 0.3px; }
  .price { font-family: "Poppins", sans-serif; font-weight: 700; font-size: 15px; line-height: 1; color: var(--ink); width: 80px; text-align: center; }
</style>
</head>
<body>
<div class="canvas">
  <main class="menu-sheet">
    <h1 class="title title--lunch">LUNCH</h1>
    <div class="title title--menu">MENU</div>
    <p class="service-note">Tuesday-Saturday 12-2pm<br>All burgers and wraps served<br>with a side of chips</p>

    <div class="brand-band"></div>
    <div class="brand-name">Saltbush Tavern</div>

    <div class="photo photo--right" role="img" aria-label="Photo of a tall stacked burger with chicken, beef patty, bacon, lettuce and tomato"></div>
    <div class="photo photo--left" role="img" aria-label="Photo of a cheeseburger with lettuce, tomato and melted cheese"></div>

    <!-- Burgers table -->
    <div class="section-label" style="left:42px; top:316px;">MENU</div>
    <div class="col-head" style="left:292px; top:321px;">NON-MEMBER</div>
    <div class="col-head" style="left:380px; top:321px;">MEMBER</div>
    <div class="rule" style="left:290px; top:319px; height:292px;"></div>
    <div class="rule" style="left:380px; top:319px; height:292px;"></div>

    <div class="dish-name" style="left:42px; top:355px;">CHICKEN BURGER</div>
    <div class="dish-desc" style="left:42px; top:374px;">Fried Greenfield Meats crumbed chicken thigh,<br>cheese, tomato, spanish onion with aioli</div>
    <div class="price" style="left:292px; top:370px;">$18.00</div>
    <div class="price" style="left:380px; top:370px;">$17.00</div>

    <div class="dish-name" style="left:42px; top:417px;">BEEF BURGER</div>
    <div class="dish-desc" style="left:42px; top:436px;">Grilled angus beef patty, lettuce, cheese,<br>beetroot, tomato, spanish onion, pickles,<br>caramelised onion with aioli</div>
    <div class="price" style="left:292px; top:432px;">$18.00</div>
    <div class="price" style="left:380px; top:432px;">$17.00</div>

    <div class="dish-name" style="left:42px; top:492px;">STEAK BURGER</div>
    <div class="dish-desc" style="left:42px; top:511px;">Grilled Greenfield Meats rib fillet, lettuce,<br>tomato, spanish onion, beetroot, cheese,<br>caramelised onion with bbq sauce</div>
    <div class="price" style="left:292px; top:507px;">$20.00</div>
    <div class="price" style="left:380px; top:507px;">$19.00</div>

    <div class="dish-name" style="left:42px; top:567px;">BARRAMUNDI BURGER</div>
    <div class="dish-desc" style="left:42px; top:586px;">Southern fried barramundi, lettuce, coleslaw<br>with homemade dill and chives aioli</div>
    <div class="price" style="left:292px; top:582px;">$18.00</div>
    <div class="price" style="left:380px; top:582px;">$17.00</div>

    <!-- Salads & wraps table -->
    <div class="rule" style="left:533px; top:673px; height:291px;"></div>
    <div class="rule" style="left:622px; top:673px; height:291px;"></div>

    <div class="dish-name" style="left:286px; top:671px;">CAESAR SALAD</div>
    <div class="dish-desc" style="left:286px; top:690px;">Cos lettuce, croutons, parmesan cheese,<br>boiled egg, caesar dressing</div>
    <div class="price" style="left:536px; top:685px;">$17.00</div>
    <div class="price" style="left:624px; top:685px;">$16.00</div>

    <div class="addon" style="left:286px; top:721px;">ADD CHICKEN</div>
    <div class="price" style="left:536px; top:721px;">$17.00</div>
    <div class="price" style="left:624px; top:721px;">$16.00</div>

    <div class="addon" style="left:286px; top:744px;">ADD CALAMARI</div>
    <div class="price" style="left:536px; top:744px;">$17.00</div>
    <div class="price" style="left:624px; top:744px;">$16.00</div>

    <div class="dish-name" style="left:286px; top:782px;">WRAP IT -</div>
    <div class="dish-desc" style="left:286px; top:800px;">Chicken caesar salad wrap</div>
    <div class="price" style="left:536px; top:796px;">$18.00</div>
    <div class="price" style="left:624px; top:796px;">$16.00</div>

    <div class="dish-name" style="left:286px; top:828px;">HONEY MUSTARD<br>CHICKEN SALAD</div>
    <div class="dish-desc" style="left:286px; top:865px;">Mesclun mix, continental cucumber,<br>cherry tomato, spanish onion, crispy chicken<br>tende (breast)</div>
    <div class="price" style="left:536px; top:844px;">$18.00</div>
    <div class="price" style="left:624px; top:844px;">$17.00</div>

    <div class="dish-name" style="left:286px; top:922px;">BANGIN' BEEF BURRITO</div>
    <div class="dish-desc" style="left:286px; top:940px;">Minced beef, sliced beef sausage, rice,<br>tomato puree, herbs</div>
    <div class="price" style="left:536px; top:937px;">$20.00</div>
    <div class="price" style="left:624px; top:937px;">$18.00</div>
  </main>
</div>
</body>
</html>
```